Business Card Design Project

We need a business card design for a new company focused on educational technology called 'Bright Harbor Educational Consulting'. We are a consulting company that helps other technology companies and schools market their solutions.

The final design should communicate the positive future of education, which is digital.

Industry/Entity Type

Business

Requirements
Nice to have
• four color, front and back.

```html
<!DOCTYPE html>
<html lang="en">
<head>
<meta charset="utf-8">
<title>Bright Harbor Educational Consulting – Business Cards</title>
<link href="https://fonts.googleapis.com/css2?family=Open+Sans:wght@400;600&display=swap" rel="stylesheet">
<style>
  :root {
    --page-bg: #e4e5e8;
    --card-white: #ffffff;
    --ink: #2b2d3c;
    --ink-soft: #44465a;
    --brand-green: #5cb82e;
    --brand-blue: #3558a3;
    --brand-blue-deep: #27438a;
    --card-shadow: 0 10px 28px rgba(0,0,0,0.22);
  }
  * { box-sizing: border-box; margin: 0; padding: 0; }
  html, body {
    width: 1200px; height: 944px; overflow: hidden;
    background: var(--page-bg);
    font-family: "Open Sans", Arial, sans-serif;
    color: var(--ink);
  }
  .canvas { position: relative; width: 1200px; height: 944px; }

  .card {
    position: absolute;
    width: 640px; height: 366px;
    background: var(--card-white);
    border-radius: 26px;
    box-shadow: var(--card-shadow);
    overflow: hidden;
  }
  .card--front { left: 70px; top: 70px; }
  .card--back  { left: 490px; top: 508px; }

  /* Brand lockup */
  .brand { display: flex; align-items: center; gap: 16px; color: var(--ink); font-weight: 400; }
  .brand__mark { width: 26px; height: 26px; background: var(--ink); flex: none; }
  .brand__name { line-height: 1; letter-spacing: 0.5px; }
  .brand__name .line-main { display: block; text-transform: uppercase; }
  .brand__name .line-sub { display: block; text-transform: uppercase; letter-spacing: 5px; margin-top: 6px; }

  .card--front .brand { position: absolute; left: 120px; top: 120px; }
  .card--front .brand__mark { width: 38px; height: 38px; }
  .card--front .line-main { font-size: 34px; }
  .card--front .line-sub { font-size: 13px; }
  .front-url {
    position: absolute; left: 140px; top: 262px;
    font-size: 17px; letter-spacing: 1.6px; color: var(--ink);
  }

  .card--back .brand { position: absolute; left: 44px; top: 38px; gap: 10px; }
  .card--back .line-main { font-size: 22px; }
  .card--back .line-sub { font-size: 8.5px; letter-spacing: 3.6px; margin-top: 4px; }

  .back-panel { position: absolute; inset: 0; }

  .contact {
    position: absolute; left: 40px; top: 120px;
    list-style: none; font-size: 15px; line-height: 1.15; color: var(--ink-soft);
  }
  .contact li { display: flex; gap: 8px; align-items: flex-start; margin-bottom: 8px; }
  .contact .icon { width: 13px; height: 13px; flex: none; margin-top: 3px; fill: var(--brand-green); }
  .contact .address { margin-bottom: 14px; }
  .contact .web .accent { color: var(--brand-green); }

  .person {
    position: absolute; right: 40px; bottom: 62px; text-align: center; color: #fff;
  }
  .person__name { font-size: 22px; font-weight: 400; letter-spacing: 0.6px; }
  .person__role { font-size: 14px; margin-top: 2px; }
</style>
</head>
<body>
<main class="canvas">

  <section class="card card--front" aria-label="Business card front">
    <div class="brand">
      <span class="brand__mark" aria-hidden="true"></span>
      <span class="brand__name">
        <span class="line-main">Bright Harbor</span>
        <span class="line-sub">Educational Consulting</span>
      </span>
    </div>
    <p class="front-url">www.brightharboredu.com</p>
  </section>

  <section class="card card--back" aria-label="Business card back">
    <svg class="back-panel" viewBox="0 0 640 366" preserveAspectRatio="none" aria-hidden="true">
      <defs>
        <linearGradient id="blueFill" x1="0" y1="0" x2="1" y2="1">
          <stop offset="0" stop-color="var(--brand-blue)"/>
          <stop offset="1" stop-color="var(--brand-blue-deep)"/>
        </linearGradient>
      </defs>
      <path d="M385 0 C 335 95, 430 240, 345 366 L640 366 L640 0 Z" fill="var(--brand-green)"/>
      <path d="M430 0 C 380 95, 470 240, 395 366 L640 366 L640 0 Z" fill="url(#blueFill)"/>
    </svg>

    <div class="brand">
      <span class="brand__mark" aria-hidden="true"></span>
      <span class="brand__name">
        <span class="line-main">Bright Harbor</span>
        <span class="line-sub">Educational Consulting</span>
      </span>
    </div>

    <ul class="contact">
      <li class="address">
        <svg class="icon" viewBox="0 0 16 16"><path d="M8 1 L15 8 H13 V15 H9.5 V10.5 H6.5 V15 H3 V8 H1 Z"/></svg>
        <span>P.O Box 582<br>Lake Meadow<br>Ohio 43102-0582</span>
      </li>
      <li>
        <svg class="icon" viewBox="0 0 16 16"><path d="M4 1 L6.5 1 L7.5 5 L5.8 6.3 C6.6 8 8 9.4 9.7 10.2 L11 8.5 L15 9.5 L15 12 C15 13.7 13.7 15 12 15 C6 15 1 10 1 4 C1 2.3 2.3 1 4 1 Z"/></svg>
        <span>555 214 7390</span>
      </li>
      <li>
        <svg class="icon" viewBox="0 0 16 16"><path d="M2 3 H14 V5 H2 Z M2 6 H14 V13 H2 Z M4 8 H12 V9 H4 Z"/></svg>
        <span>555 000 0000</span>
      </li>
      <li>
        <svg class="icon" viewBox="0 0 16 16"><path d="M1 3 H15 V13 H1 Z M1.5 3.5 L8 9 L14.5 3.5" fill="var(--brand-green)" stroke="#fff" stroke-width="1"/></svg>
        <span>brightharboredu.com</span>
      </li>
      <li class="web">
        <svg class="icon" viewBox="0 0 16 16"><circle cx="8" cy="8" r="7"/></svg>
        <span>www.<span class="accent">brightharboredu</span>.com</span>
      </li>
    </ul>

    <div class="person">
      <p class="person__name">Daniel Marsh</p>
      <p class="person__role">director</p>
    </div>
  </section>

</main>
</body>
</html>
```